Top International Talent Management Needs creative business card design

We manage actors careers and book them liaising and promoting their profiles internationally through Casting Directors, Producers, Directors, Publicists etc. We need clearly visable contact details but with a design that reflects our status and creativity of TV, Feature Film industry. Our logo is attached and needs to relate and our website is www.marrowlanepeople.com
No flame designs please but please incorporate logo colours.

Target Market(s)

Clients

Industry/Entity Type

Film Production

Contact Information for Business Card

Director Rosalind Tebbett
Suite F, Building 4, Harrowgate Sound Stages, Tullick Vale, Sydney, NSW 2021

Font styles to use
Sans Serif

Colors
ec1f27

Requirements
Nice to have
• Colours should relate to logo attached and type can relate again to type in the logo design.
Should not have
• No Flames designs and best to be not too obvious with the film designs eiither. Needs to be more creative and modern

```html
<!DOCTYPE html>
<html lang="en">
<head>
<meta charset="utf-8">
<title>Marrow Lane People — Business Card</title>
<link rel="stylesheet" href="https://fonts.googleapis.com/css2?family=Orbitron:wght@400;700&family=Exo+2:wght@600;700&display=swap">
<style>
  :root {
    --brand-red: #ec1f27;
    --deep-red: #a9151b;
    --ink: #111111;
    --card-black: #121212;
    --panel-grey: #2f2f2f;
    --text-light: #f2f2f2;
    --text-soft: #c9c9c9;
    --band-white: #ffffff;
    --band-shade: #d6d6d6;
    --backdrop: #dcdcdc;
  }
  * { box-sizing: border-box; margin: 0; padding: 0; }
  html, body { width: 1200px; height: 900px; overflow: hidden; }
  body {
    background: var(--backdrop);
    position: relative;
    font-family: "Exo 2", sans-serif;
  }
  .card {
    position: absolute;
    left: 260px;
    width: 680px;
    height: 400px;
    overflow: hidden;
  }

  /* ---------- Back card ---------- */
  .card-back { top: 40px; background: var(--card-black); }
  .card-back .brand {
    position: absolute; left: 40px; top: 30px;
  }
  .card-back .brand-name {
    font-family: "Orbitron", sans-serif; font-weight: 700;
    font-size: 30px; letter-spacing: 1px; color: var(--brand-red);
  }
  .card-back .brand-web {
    margin-top: 6px;
    font-family: "Exo 2", sans-serif; font-weight: 600;
    font-size: 17px; color: var(--text-light); letter-spacing: 0.5px;
  }
  .card-back .email {
    position: absolute; right: 34px; top: 64px;
    font-size: 11px; font-weight: 600; color: var(--text-soft);
  }
  .card-back .corner-tab {
    position: absolute; right: 14px; top: 60px;
  }
  .audience-list {
    position: absolute; left: 0; top: 150px; width: 262px;
    list-style: none;
  }
  .audience-list li {
    display: flex; align-items: center; gap: 10px;
    height: 34px; padding-left: 14px;
    font-weight: 700; font-size: 15px; letter-spacing: 0.5px;
    color: var(--text-light); text-transform: uppercase;
  }
  .audience-list li.is-active { background: var(--brand-red); padding-left: 20px; }
  .audience-list li:not(.is-active) { padding-left: 20px; }
  .audience-list svg { flex: none; }
  .phone-band {
    position: absolute; left: 262px; right: 0; top: 144px; height: 48px;
    background: var(--brand-red);
    display: flex; align-items: center; padding-left: 14px;
    font-family: "Orbitron", sans-serif; font-weight: 400;
    font-size: 30px; letter-spacing: 2px; color: var(--ink);
  }
  .about-panel {
    position: absolute; left: 262px; right: 0; top: 192px; bottom: 0;
    background: var(--panel-grey);
    display: flex; align-items: flex-start; justify-content: center;
    padding: 26px 28px 0;
  }
  .about-panel p {
    font-family: "Orbitron", sans-serif; font-weight: 400;
    font-size: 12.5px; line-height: 1.75; letter-spacing: 1px;
    color: var(--text-soft); text-align: center; text-transform: uppercase;
  }

  /* ---------- Front card ---------- */
  .card-front {
    top: 460px;
    background: linear-gradient(90deg, var(--brand-red) 0%, var(--deep-red) 100%);
  }
  .card-front .web {
    position: absolute; right: 120px; top: 40px;
    font-weight: 600; font-size: 17px; letter-spacing: 2px;
    color: var(--text-light);
  }
  .name-band {
    position: absolute; left: 0; right: 0; top: 120px; height: 130px;
    background: linear-gradient(90deg, var(--band-shade) 0%, var(--band-white) 55%, var(--band-shade) 100%);
    display: flex; align-items: center; justify-content: center;
  }
  .name-band .brand-name {
    font-family: "Orbitron", sans-serif; font-weight: 700;
    font-size: 38px; letter-spacing: 2px; color: var(--deep-red);
  }
  .card-front .address {
    position: absolute; left: 30px; bottom: 34px;
    white-space: nowrap;
    font-weight: 700; font-size: 12.5px; letter-spacing: 0.4px;
    color: var(--text-light); text-transform: uppercase;
  }
</style>
</head>
<body>

  <section class="card card-back">
    <div class="brand">
      <div class="brand-name">MARROW LANE</div>
      <div class="brand-web">marrowlanepeople.com</div>
    </div>
    <div class="email">talent@marrowlanepeople.com</div>
    <svg class="corner-tab" width="12" height="12" viewBox="0 0 12 12" aria-hidden="true">
      <polygon points="0,0 12,0 12,12" fill="var(--brand-red)"/>
    </svg>

    <ul class="audience-list">
      <li class="is-active"><svg width="9" height="10" viewBox="0 0 9 10" aria-hidden="true"><polygon points="0,0 9,5 0,10" fill="#fff"/></svg>Casting Directors</li>
      <li><svg width="9" height="10" viewBox="0 0 9 10" aria-hidden="true"><polygon points="0,0 9,5 0,10" fill="#fff"/></svg>Producers</li>
      <li><svg width="9" height="10" viewBox="0 0 9 10" aria-hidden="true"><polygon points="0,0 9,5 0,10" fill="#fff"/></svg>Directors</li>
      <li><svg width="9" height="10" viewBox="0 0 9 10" aria-hidden="true"><polygon points="0,0 9,5 0,10" fill="#fff"/></svg>TV Industries</li>
    </ul>

    <div class="phone-band">+61 0 491570156</div>
    <div class="about-panel">
      <p>Marrow Lane People is a<br>premier management company<br>representing artists in all<br>key international markets<br>including motion picture,<br>television, voice and<br>theatrical industries.</p>
    </div>
  </section>

  <section class="card card-front">
    <div class="web">www.marrowlanepeople.com</div>
    <div class="name-band">
      <div class="brand-name">MARROW LANE PEOPLE</div>
    </div>
    <div class="address">Suite F, Building 4, Harrowgate Sound Stages, Tullick Vale, Sydney, NSW 2021</div>
  </section>

</body>
</html>
```